Brimovex business card

Based on company logo and website given , to design a business card temple. Slogan "Your furry friends deserves the best"
Color style please refer to our website

```html
<!DOCTYPE html>
<html lang="en">
<head>
<meta charset="utf-8">
<title>Brimovex Business Card</title>
<link href="https://fonts.googleapis.com/css2?family=Montserrat:wght@400;500;600&display=swap" rel="stylesheet">
<style>
  :root {
    --ink-green: #092b2a;
    --brand-yellow: #ffd600;
    --paper: #efeff1;
    --backdrop: #ececec;
    --text-grey: #3d4343;
    --white: #ffffff;
  }
  * { margin: 0; padding: 0; box-sizing: border-box; }
  html, body {
    width: 1200px;
    height: 1200px;
    overflow: hidden;
    background: var(--backdrop);
    font-family: "Montserrat", sans-serif;
  }
  .canvas { position: relative; width: 1200px; height: 1200px; }

  .card {
    position: absolute;
    left: 286px;
    width: 634px;
    height: 380px;
    border-radius: 30px;
    overflow: hidden;
  }
  .card--front { top: 165px; background: var(--ink-green); }
  .card--back { top: 668px; background: var(--paper); }

  .brand-name {
    position: absolute;
    font-family: "Montserrat", sans-serif;
    font-weight: 600;
    color: var(--brand-yellow);
    font-size: 54px;
    letter-spacing: -0.5px;
    line-height: 1;
    white-space: nowrap;
    transform: translateX(-50%);
  }
  .card--front .brand-name { left: 317px; top: 170px; }
  .card--back .brand-name { left: 174px; top: 171px; }

  .tagline {
    position: absolute;
    left: 0;
    width: 100%;
    top: 242px;
    text-align: center;
    color: var(--white);
    font-size: 14.5px;
    font-weight: 400;
  }

  .person-name {
    position: absolute;
    left: 346px;
    top: 96px;
    color: var(--ink-green);
    font-size: 29px;
    font-weight: 600;
  }
  .name-rule {
    position: absolute;
    left: 346px;
    right: 0;
    top: 136px;
    height: 4px;
    background: var(--ink-green);
  }
  .job-title {
    position: absolute;
    left: 346px;
    top: 148px;
    color: var(--text-grey);
    font-size: 17px;
    font-weight: 400;
    letter-spacing: 1.6px;
  }
  .contact-list {
    position: absolute;
    left: 346px;
    top: 198px;
    list-style: none;
  }
  .contact-item {
    display: flex;
    align-items: center;
    height: 30.3px;
    color: var(--text-grey);
    font-size: 13.5px;
    letter-spacing: 1.3px;
  }
  .contact-icon {
    width: 18px;
    height: 18px;
    margin-right: 17px;
    fill: var(--ink-green);
    flex: none;
  }
</style>
</head>
<body>
<main class="canvas">
  <section class="card card--front">
    <div class="brand-name">Brimovex</div>
    <p class="tagline">Your furry friends deserves the best</p>
  </section>

  <section class="card card--back">
    <div class="brand-name">Brimovex</div>
    <h1 class="person-name">John Doe</h1>
    <div class="name-rule"></div>
    <p class="job-title">Executive Manager</p>
    <ul class="contact-list">
      <li class="contact-item">
        <svg class="contact-icon" viewBox="0 0 24 24"><path d="M19 2l3 3-2 3c-1 6-6 12-13 13l-3 1-2-3 4-3 2 2c3-1 6-5 7-8l-2-2z"/></svg>
        0123-456-789
      </li>
      <li class="contact-item">
        <svg class="contact-icon" viewBox="0 0 24 24"><path d="M12 1a8 8 0 0 0-8 8c0 6 8 14 8 14s8-8 8-14a8 8 0 0 0-8-8zm0 11a3 3 0 1 1 0-6 3 3 0 0 1 0 6z"/></svg>
        Lorem Ipsum Dolor Sit Amet
      </li>
      <li class="contact-item">
        <svg class="contact-icon" viewBox="0 0 24 24"><circle cx="12" cy="12" r="10" fill="none" stroke="#092b2a" stroke-width="2.4"/><path d="M7 6l4 1 1 3-3 2 1 4-3-2-2-4zM14 13l4 1-1 4-3 2z"/></svg>
        www.websitename.com
      </li>
      <li class="contact-item">
        <svg class="contact-icon" viewBox="0 0 24 24"><path d="M1 5h22v14H1z M3 6.5l9 7 9-7" fill="var(--ink-green)"/><path d="M2 6l10 8 10-8M2 18l7-6M22 18l-7-6" fill="none" stroke="#efeff1" stroke-width="1.4"/></svg>
        name@sitename.com
      </li>
    </ul>
  </section>
</main>
</body>
</html>
```